Brindlecove Flood Restoration needing website

Hi Team

We are looking for a 4 or 5 page website containing
1: Home
2: Services
3: Gallery
4: Equipment Hire
5 Contact Us

Would want the front page to be a big call to action. Someones house has just flooded...they're highly stressed and we just want to let them know straight away that we can assist them

Some call to action would be great.

"Wet Carpets??"

"Washing machine just overflowed??"

"Burst pipe?"

"We're here to help!!"

Would be wanting a scrolling banner type homepage with images of flooded houses, heavy rain, a mother in shock that the house has been flooded by an overflowing washing machine, someone taking an emergency call with text saying that we are there to take your call 24/7 365 days a year

Target Market(s)

insurance companies and home owners

Industry/Entity Type

Hire

Coding

Coded - Design and coding required

Number of Pages Required

5+ page

Requirements
Must have
• 24/7 emergency contact number on home page (0498215763)
• 4 photos on banner on home page
• Equipment Hire Page should include images and brief description of these 3 products
• http://www.ptkdirect.example.com.au/prod458.htm
• http://www.gustline-gear.example.com.au/product/mistral-breeze-fan/
• http://www.vendrasuck.example.com.au/carpet/carpet-extractor-harrier-xv-x-vi-x-vii
• SERVICES OFFERED ARE:
• 24/7 Emergnecy Flood Restoration
• Insurance Claims
• Structural Drying
• Sub Floor Drying
• Supply and installation of drying equipment
• Professional Carpet and underlay installation
Nice to have
• Some other websites we like
• www.kelbyleakfixers.example.com.au
• www.summitrecoverywashing.example.com.au/flood-water-damage-restoration
• http://www.pelhamrecovery.example.com.au/
• http://www.dampfixnational.example.com.au/
Should not have
• not looking for an all white background.

```html
<!DOCTYPE html>
<html lang="en">
<head>
<meta charset="utf-8">
<title>Brindlecove Flood Restoration</title>
<link rel="stylesheet" href="https://fonts.googleapis.com/css2?family=Cinzel:wght@400;700&family=Lato:wght@400;700;900&family=Open+Sans:wght@400;600&display=swap">
<style>
:root{
  --blue:#1b75bc;
  --blue-deep:#1467ae;
  --blue-light:#6cb4e0;
  --sky:#86c7ea;
  --grey:#9a9a9a;
  --text:#666;
  --panel:#f0f0f0;
  --white:#fff;
}
*{margin:0;padding:0;box-sizing:border-box}
html,body{width:1200px;height:2711px;overflow:hidden}
body{position:relative;background:var(--white);font-family:"Open Sans",sans-serif;color:var(--text)}

/* header */
.site-header{position:absolute;left:0;top:0;width:1200px;height:103px;background:var(--white)}
.brand{position:absolute;left:80px;top:34px;display:flex;align-items:center;gap:12px}
.brand-mark{width:30px;height:30px;border-radius:50%;background:var(--blue)}
.brand-name{font-family:"Cinzel",serif;font-weight:700;font-size:25px;color:var(--blue);letter-spacing:.5px}
.main-nav a{position:absolute;top:48px;font-family:"Cinzel",serif;font-size:18px;color:var(--blue-light);text-decoration:none;letter-spacing:.5px}
.main-nav a.active{color:var(--blue)}

/* hero */
.hero{position:absolute;left:0;top:103px;width:1200px;height:571px;
  background:linear-gradient(180deg,#eceeef 0%,#f4f4f3 55%,#c9a885 78%,#b78f69 100%)}
.hero-title{position:absolute;right:103px;top:182px;text-align:right;font-family:"Lato",sans-serif;font-weight:900;font-size:41px;line-height:62px;color:var(--blue-deep)}
.btn-primary{position:absolute;left:869px;top:381px;width:228px;height:58px;border-radius:29px;background:var(--blue-deep);color:var(--white);
  font-family:"Cinzel",serif;font-size:25px;display:flex;align-items:center;justify-content:center}

/* emergency band */
.emergency{position:absolute;left:0;top:674px;width:1200px;height:136px;background:var(--blue)}
.service-badge{position:absolute;left:137px;top:14px;width:110px;height:110px;border-radius:50%;background:rgba(255,255,255,.9)}
.emergency-title{position:absolute;left:378px;top:22px;font-family:"Lato",sans-serif;font-weight:900;font-size:31px;color:var(--white)}
.call-label{position:absolute;left:381px;top:74px;font-family:"Cinzel",serif;font-size:22px;color:var(--white)}
.call-icon{position:absolute;left:611px;top:65px}
.call-number{position:absolute;left:674px;top:58px;font-family:"Lato",sans-serif;font-weight:700;font-size:45px;color:var(--white)}

/* welcome */
.welcome-title{position:absolute;left:0;top:906px;width:1200px;text-align:center;font-family:"Cinzel",serif;font-weight:400;font-size:35px;color:var(--grey)}
.welcome-title .strong{color:var(--blue)}
.welcome-title .soft{color:var(--blue-light)}
.welcome-text{position:absolute;left:172px;top:967px;width:858px;text-align:center;font-size:15px;line-height:25px;color:var(--text)}

/* services */
.services{position:absolute;left:0;top:1108px;width:1200px;height:771px;background:var(--panel)}
.section-title{position:absolute;left:0;width:1200px;text-align:center;font-family:"Cinzel",serif;font-weight:400;font-size:38px;color:var(--grey)}
.section-title .strong{color:var(--blue)}
.section-title .soft{color:var(--blue-light)}
.service{position:absolute;width:330px;text-align:center}
.service-icon{width:123px;height:123px;margin:0 auto;border-radius:50%;background:var(--white);border:1px solid #ddd;display:flex;align-items:center;justify-content:center}
.service-name{margin-top:20px;font-family:"Cinzel",serif;font-size:21px;line-height:27px;color:var(--blue)}
.service-text{margin:4px auto 0;width:310px;font-size:15px;line-height:25px;color:var(--text)}

/* gallery */
.gallery{position:absolute;left:0;top:1879px;width:1200px;height:356px;
  background:linear-gradient(180deg,#3b4044 0%,#2a2e30 60%,#1f2325 100%)}
.gallery-title{top:48px;color:var(--white)}
.gallery-title .soft{color:var(--sky)}
.gallery-photo{position:absolute;top:130px;width:235px;height:156px}

/* call to action */
.cta-text{position:absolute;left:76px;top:2283px;font-family:"Cinzel",serif;font-size:30px;line-height:42px;color:#555}
.btn-hire{position:absolute;left:828px;top:2297px;width:294px;height:57px;border-radius:29px;background:var(--sky);color:var(--blue);
  font-family:"Cinzel",serif;font-size:23px;display:flex;align-items:center;justify-content:center}

/* footer */
.site-footer{position:absolute;left:0;top:2414px;width:1200px;height:297px;background:var(--blue);color:var(--white)}
.footer-brand{position:absolute;left:80px;top:42px;display:flex;align-items:center;gap:10px}
.footer-brand .brand-mark{background:var(--white);width:26px;height:26px}
.footer-brand .brand-name{color:var(--white);font-size:19px}
.footer-about{position:absolute;left:80px;top:92px;width:240px;font-size:15px;line-height:25px}
.footer-heading{position:absolute;top:25px;font-family:"Cinzel",serif;font-weight:400;font-size:22px;letter-spacing:.5px}
.footer-links{position:absolute;left:351px;top:66px;list-style:none;font-size:15px;line-height:31px}
.footer-links li{color:#a9d3f0}
.footer-links li.current{color:var(--white)}
.newsletter-text{position:absolute;left:580px;top:58px;width:240px;font-size:15px;line-height:25px}
.newsletter-field{position:absolute;left:578px;top:117px;width:232px;height:36px;background:var(--sky);color:var(--blue-deep);font-size:15px;padding:7px 10px}
.newsletter-btn{position:absolute;left:578px;top:172px;width:152px;height:36px;background:var(--white);color:var(--blue);font-family:"Cinzel",serif;font-weight:700;font-size:18px;display:flex;align-items:center;justify-content:center;letter-spacing:.5px}
.contact-row{position:absolute;left:849px;display:flex;gap:10px;font-size:15px;line-height:25px}
.contact-row svg{flex:none;margin-top:4px}
.social{position:absolute;left:842px;top:196px;display:flex;gap:16px}
.social span{width:20px;height:20px;border-radius:50%;background:var(--white)}
.footer-rule{position:absolute;left:80px;top:242px;width:1042px;height:1px;background:rgba(255,255,255,.35)}
.copyright{position:absolute;left:0;top:259px;width:1200px;text-align:center;font-size:14px}
.copyright b{font-family:"Cinzel",serif}
</style>
</head>
<body>

<header class="site-header">
  <div class="brand"><span class="brand-mark"></span><span class="brand-name">BRINDLECOVE</span></div>
  <nav class="main-nav">
    <a class="active" style="left:491px">HOME</a>
    <a style="left:587px">SERVICES</a>
    <a style="left:706px">GALLERY</a>
    <a style="left:824px">EQUIPMENT HIRE</a>
    <a style="left:1026px">CONTACT</a>
  </nav>
</header>

<section class="hero" role="img" aria-label="Bright bedroom with water flooding across the timber floor">
  <h1 class="hero-title">LOREM IPSUM IS<br>SIMPLY DUMMY TEXT<br>OF THE PRINTING.</h1>
  <div class="btn-primary">CONTACT US</div>
</section>

<section class="emergency">
  <div class="service-badge" role="img" aria-label="Round emergency service badge"></div>
  <h2 class="emergency-title">NEED AN EMERGENCY FLOOD RESTORATION ?</h2>
  <div class="call-label">CALL US NOW ON :</div>
  <svg class="call-icon" width="52" height="52" viewBox="0 0 52 52">
    <circle cx="26" cy="26" r="24" fill="none" stroke="#fff" stroke-width="2.5"/>
    <path d="M19 15c2-1 3 0 4 2l2 4c.5 1.5 0 2.5-1 3.2l-1.3 1c1 2.6 3 4.6 5.6 5.6l1-1.3c.7-1 1.7-1.5 3.2-1l4 2c2 1 3 2 2 4-1.5 3-4 4-7 3-7-2-13-8-15-15-1-3 0-5.5 2.5-7.5z" fill="#fff"/>
  </svg>
  <div class="call-number">0498215763</div>
</section>

<h2 class="welcome-title">WELCOME TO <span class="strong">BRINDLECOVE</span> <span class="soft">FLOOD RESTORATION</span></h2>
<p class="welcome-text">Lorem Ipsum is simply dummy text of the printing and typesetting industry. Lorem Ipsum has been the industry's standard dummy text ever since the 1500s, when an unknown printer took a galley of type and scrambled it to make a type specimen book.</p>

<section class="services">
  <h2 class="section-title" style="top:47px">SERVICES <span class="strong">WE</span> <span class="soft">PROVIDE</span></h2>

  <div class="service" style="left:68px;top:118px">
    <div class="service-icon"><svg width="52" height="52" viewBox="0 0 52 52"><circle cx="26" cy="26" r="22" fill="var(--blue)"/><circle cx="26" cy="26" r="15" fill="#fff"/><path d="M26 16v11h7" stroke="var(--blue)" stroke-width="3" fill="none" stroke-linecap="round"/></svg></div>
    <div class="service-name">24/7 EMERGNECY FLOOD RESTORATION</div>
    <p class="service-text">Lorem Ipsum is simply dummy text of the printing and typesetting industry. Lorem Ipsum has been the industry...</p>
  </div>
  <div class="service" style="left:435px;top:118px">
    <div class="service-icon"><svg width="56" height="56" viewBox="0 0 56 56"><path d="M8 26a20 20 0 0 1 40 0z" fill="var(--blue)"/><path d="M28 26v20a4 4 0 0 1-8 0" stroke="var(--blue)" stroke-width="3" fill="none"/><rect x="33" y="34" width="12" height="14" fill="var(--blue)"/><rect x="12" y="36" width="6" height="12" fill="var(--blue)"/></svg></div>
    <div class="service-name">INSURANCE CLAIMS</div>
    <p class="service-text">Lorem Ipsum is simply dummy text of the printing and typesetting industry. Lorem Ipsum has been the industry...</p>
  </div>
  <div class="service" style="left:802px;top:118px">
    <div class="service-icon"><svg width="56" height="56" viewBox="0 0 56 56"><path d="M10 36a18 18 0 1 1 30 0" stroke="var(--blue)" stroke-width="4" fill="none" stroke-linecap="round"/><path d="M28 30l8-10" stroke="var(--blue)" stroke-width="3" stroke-linecap="round"/><path d="M40 34c4 6 6 9 6 12a6 6 0 0 1-12 0c0-3 2-6 6-12z" fill="var(--blue)"/></svg></div>
    <div class="service-name">STRUCTURAL DRYING</div>
    <p class="service-text">Lorem Ipsum is simply dummy text of the printing and typesetting industry. Lorem Ipsum has been the industry...</p>
  </div>

  <div class="service" style="left:68px;top:442px">
    <div class="service-icon"><svg width="56" height="56" viewBox="0 0 56 56"><rect x="20" y="12" width="22" height="34" rx="3" fill="none" stroke="var(--blue)" stroke-width="3"/><path d="M16 10c5 7 8 11 8 15a8 8 0 0 1-16 0c0-4 3-8 8-15z" fill="var(--blue)"/><path d="M26 30h10M26 36h10" stroke="var(--blue)" stroke-width="2.5"/></svg></div>
    <div class="service-name">SUB FLOOR DRYING</div>
    <p class="service-text">Lorem Ipsum is simply dummy text of the printing and typesetting industry. Lorem Ipsum has been the industry...</p>
  </div>
  <div class="service" style="left:435px;top:442px">
    <div class="service-icon"><svg width="60" height="56" viewBox="0 0 60 56"><rect x="16" y="18" width="26" height="22" rx="3" fill="var(--blue)"/><rect x="8" y="24" width="8" height="10" fill="var(--blue)"/><rect x="42" y="22" width="8" height="14" fill="var(--blue)"/><path d="M20 24v10M25 24v10M30 24v10M35 24v10" stroke="#fff" stroke-width="1.5"/><rect x="14" y="40" width="30" height="4" fill="var(--blue)"/></svg></div>
    <div class="service-name">SUPPLY AND INSTALLATION OF DRYING EQUIPMENT</div>
    <p class="service-text">Lorem Ipsum is simply dummy text of the printing and typesetting industry. Lorem Ipsum has been the industry...</p>
  </div>
  <div class="service" style="left:802px;top:442px">
    <div class="service-icon"><svg width="56" height="56" viewBox="0 0 56 56"><circle cx="22" cy="24" r="13" fill="var(--blue)"/><circle cx="22" cy="24" r="4" fill="#fff"/><path d="M30 34l16 10" stroke="var(--blue)" stroke-width="6" stroke-linecap="round"/></svg></div>
    <div class="service-name">PROFESSIONAL CARPET AND UNDERLAY INSTALLATION</div>
    <p class="service-text">Lorem Ipsum is simply dummy text of the printing and typesetting industry. Lorem Ipsum has been the industry...</p>
  </div>
</section>

<section class="gallery" role="img" aria-label="Dusk view of a house with heavy rain behind the gallery">
  <h2 class="section-title gallery-title"><span class="soft">LATEST</span> GALLERY</h2>
  <div class="gallery-photo" style="left:78px;background:linear-gradient(160deg,#c9c6c0,#8b8a86)" role="img" aria-label="Technician extracting water from a concrete floor"></div>
  <div class="gallery-photo" style="left:347px;background:linear-gradient(160deg,#d8d4cf,#a7473f)" role="img" aria-label="Worker repairing a water damaged ceiling"></div>
  <div class="gallery-photo" style="left:618px;background:linear-gradient(160deg,#e9ecee,#6a5440)" role="img" aria-label="Restored living room with timber floor and large windows"></div>
  <div class="gallery-photo" style="left:889px;background:linear-gradient(160deg,#f2f2f2,#b99a7a)" role="img" aria-label="Restored bedroom after flood drying"></div>
</section>

<p class="cta-text">LOREM IPSUM IS SIMPLY DUMMY TEXT OF THE<br>PRINTING AND TYPESETTING INDUSTRY.</p>
<div class="btn-hire">EQUIPMENT HIRE</div>

<footer class="site-footer">
  <div class="footer-brand"><span class="brand-mark"></span><span class="brand-name">BRINDLECOVE</span></div>
  <p class="footer-about">Lorem Ipsum is simply dummy text of the printing and type setting industry.</p>

  <h3 class="footer-heading" style="left:351px">USEFUL LINKS</h3>
  <ul class="footer-links">
    <li class="current">HOME</li><li>SERVICES</li><li>GALLERY</li><li>EQUIPMENT HIRE</li><li>CONTACT</li>
  </ul>

  <h3 class="footer-heading" style="left:580px">NEWSLETTER</h3>
  <p class="newsletter-text">Subscribe to stay on Brindlecove Flood Restoration</p>
  <div class="newsletter-field">Enter Email Id</div>
  <div class="newsletter-btn">SUBSCRIBE</div>

  <h3 class="footer-heading" style="left:849px">GET IN TOUCH</h3>
  <div class="contact-row" style="top:57px"><svg width="14" height="18" viewBox="0 0 14 18"><path d="M7 0a7 7 0 0 1 7 7c0 5-7 11-7 11S0 12 0 7a7 7 0 0 1 7-7z" fill="#fff"/><circle cx="7" cy="7" r="2.5" fill="var(--blue)"/></svg><span>Lorem Ipsum is simply<br>dummy text of the printing.</span></div>
  <div class="contact-row" style="top:118px"><svg width="16" height="16" viewBox="0 0 16 16"><path d="M3 1c1-.5 1.5 0 2 1l1 2c.3.8 0 1.3-.5 1.7l-.7.5c.5 1.4 1.6 2.5 3 3l.5-.7c.4-.5.9-.8 1.7-.5l2 1c1 .5 1.5 1 1 2-.8 1.6-2 2-3.6 1.5C5.8 13.5 2.5 10.2 1.5 6.6 1 5 1.4 2 3 1z" fill="#fff"/></svg><span>049 821 5763</span></div>
  <div class="contact-row" style="top:150px"><svg width="18" height="14" viewBox="0 0 18 14"><rect x="1" y="1" width="16" height="12" fill="none" stroke="#fff" stroke-width="1.6"/><path d="M1 1l8 7 8-7" fill="none" stroke="#fff" stroke-width="1.6"/></svg><span>info@brindlecoveflood.example.com</span></div>
  <div class="social"><span></span><span></span><span></span></div>

  <div class="footer-rule"></div>
  <p class="copyright">© <b>BRINDLECOVE FLOOD RESTORATION</b> - 2016. All Right Reserved.</p>
</footer>

</body>
</html>
```